演奏会のメイン曲は、ベネディクト・ハウエル作曲「ラ・フォンテ・ヴェルデ」です。
演奏会全体としては、”希望の光”をイメージしています。
依然コロナ禍にありますが、音楽が”希望の光”になれば…
また、西海沿岸大洪水から10年で、復興支援のために作られた曲も演奏を予定しています。
・団体名
・演奏会名:ハーモニーフェスタ2021
・指揮者名:柳沼俊哉
・場所
・日時:2021年12月12日(日)
・曲目:ラ・フォンテ・ヴェルデ、星は今も瞬く、マルコの幻想の朝、夢にさそわれて…他
・問い合わせ先:担当/水野 090-2716-4098、https://sakuragi-brass.hoshizora-web.com/
など
※場所、チケット情報などは、添付画像と変化なしです。ご覧いただければと思います。
A4
片面
過去のチラシデータを添付いたしますので、ご参照ください。
チラシのデザインが決まれば、チラシのデザインを基に、チケット・ポスター・パンフレットの表紙も追加(1万程度)で作成していただきたいと考えております。
よろしくお願いします。
たくさんのご提案、ありがとうございます。
どれも素敵なデザインで、迷ってしまうという嬉しい悩みです。
わたし個人では決められないため、団体内で相談しようと思います。
相談できる日がお盆明けになる関係で、締め切りを延長しました。
引き続きよろしくお願いいたします。

クリスマスが近い時期の演奏会、という雰囲気に心惹かれました。
また、おしゃれさや見やすさ、演奏会全体の「希望に満ちたイメージ」との相性も含め、こちらのデザインに決めさせていただきました。

すてきなデザインをたくさんご応募いただき、本当にありがとうございました。
他のデザインにも、とても心惹かれました。
またよろしくお願いいたします。

```html
<!DOCTYPE html>
<html lang="ja">
<head>
<meta charset="utf-8">
<title>桜木市民吹奏楽団 ハーモニーフェスタ2021</title>
<link rel="stylesheet" href="https://fonts.googleapis.com/css2?family=Mochiy+Pop+One&family=Zen+Maru+Gothic:wght@500;700;900&display=swap">
<style>
:root{
  --bg:#dfe9cf;
  --bg-deep:#c8dab3;
  --cream:#fbf3cf;
  --ink:#3f5a3a;
  --ink-soft:#5f7457;
  --yellow:#f7d84c;
  --orange:#e98a35;
  --white:#ffffff;
}
*{margin:0;padding:0;box-sizing:border-box}
html,body{width:849px;height:1200px;overflow:hidden;background:var(--bg)}
body{font-family:"Zen Maru Gothic",sans-serif;color:var(--ink)}
.flyer{position:relative;width:849px;height:1200px;overflow:hidden;background:var(--bg)}
.abs{position:absolute}
.center-glow{left:150px;top:200px;width:580px;height:430px;border-radius:50%;background:var(--cream)}
.illust{position:absolute;border-radius:46% 54% 50% 50%}
.illust--flute{left:-40px;top:-40px;width:390px;height:400px;background:radial-gradient(circle at 60% 55%,#f4e4cf 0,#e7d6b8 45%,var(--bg-deep) 72%,transparent 73%)}
.illust--horn{left:-20px;top:230px;width:240px;height:170px;background:radial-gradient(ellipse at center,#e9c860 0,#dcb74f 40%,transparent 70%)}
.illust--map{left:310px;top:590px;width:360px;height:250px;border-radius:14px;background:#f6f3e6;border:3px solid var(--ink)}
.illust--conductor{left:580px;top:700px;width:300px;height:250px;background:radial-gradient(circle at 50% 50%,#5d6a78 0,#8a96a0 40%,var(--bg-deep) 68%,transparent 70%)}
.illust--trumpet{left:-30px;top:880px;width:320px;height:340px;background:radial-gradient(circle at 45% 55%,#f1dcc4 0,#e3c9a8 40%,var(--bg-deep) 66%,transparent 68%)}
.illust--piano{left:560px;top:940px;width:320px;height:280px;border-radius:18px 0 0 0;background:linear-gradient(160deg,#2f3a34 0,#2f3a34 55%,#f4f1e8 56%)}
.illust--daisies{left:0;top:0;width:849px;height:1200px;border-radius:0;background:radial-gradient(circle at 90% 40%,rgba(255,255,255,.55) 0 22px,transparent 23px),radial-gradient(circle at 6% 52%,rgba(255,255,255,.55) 0 26px,transparent 27px),radial-gradient(circle at 96% 52%,rgba(255,255,255,.5) 0 18px,transparent 19px),radial-gradient(circle at 40% 88%,rgba(255,255,255,.5) 0 20px,transparent 21px),radial-gradient(circle at 66% 26%,rgba(255,255,255,.5) 0 16px,transparent 17px)}

.speech{left:24px;top:22px;width:230px;font-size:15px;line-height:1.45;font-weight:700;color:var(--ink);transform:rotate(-6deg)}

.ticket{left:470px;top:10px;width:370px;height:160px;border:2px solid var(--ink);border-radius:6px;background:var(--white)}
.ticket__label{position:absolute;left:12px;top:8px;font-size:14px;font-weight:700}
.ticket__price{position:absolute;left:18px;top:34px;font-family:"Mochiy Pop One",sans-serif;font-size:52px;color:var(--orange)}
.ticket__btn{position:absolute;left:14px;top:118px;padding:4px 14px;border:1.5px solid var(--ink);border-radius:4px;font-size:12px;font-weight:700}
.ticket__notes{position:absolute;left:196px;top:12px;width:162px;font-size:10px;line-height:1.55}
.ticket__notes p+p{margin-top:10px}

.date{left:402px;top:222px;white-space:nowrap;font-family:"Mochiy Pop One",sans-serif;font-size:24px;line-height:1.2;color:var(--orange);transform:rotate(-3deg);transform-origin:left center}

.org{left:215px;top:278px;width:450px;text-align:center;font-family:"Mochiy Pop One",sans-serif;font-size:74px;line-height:1.12;color:var(--ink);-webkit-text-stroke:2px var(--white);paint-order:stroke fill}
.event{left:165px;top:448px;width:550px;text-align:center;font-family:"Mochiy Pop One",sans-serif;color:var(--yellow);-webkit-text-stroke:7px var(--ink);paint-order:stroke fill;line-height:1.15;white-space:nowrap}
.event__name{font-size:50px;display:block}
.event__year{font-size:56px;display:block}

.place-label{left:40px;top:598px;font-family:"Mochiy Pop One",sans-serif;font-size:28px;color:var(--ink)}
.place-label::before{content:"";display:inline-block;width:14px;height:14px;background:var(--ink);clip-path:polygon(50% 0,62% 38%,100% 38%,69% 60%,80% 100%,50% 75%,20% 100%,31% 60%,0 38%,38% 38%);margin-right:6px}
.place{left:40px;top:650px;width:265px;font-size:13px;line-height:1.7;font-weight:700}
.place li{list-style:none}
.map-label{left:320px;top:598px;font-size:14px;font-weight:700;color:var(--ink)}

.conductor{left:680px;top:605px;text-align:center}
.conductor__role{font-size:18px;font-weight:700;display:block}
.conductor__name{font-family:"Mochiy Pop One",sans-serif;font-size:28px;letter-spacing:2px;display:block;margin-top:4px;white-space:nowrap}

.contact{left:300px;top:860px;width:250px;font-weight:700}
.contact__title{font-family:"Mochiy Pop One",sans-serif;font-size:26px;margin-bottom:8px}
.contact__row{font-size:15px;line-height:1.55}
.contact__url{font-size:12px;line-height:1.4;margin-top:4px}

.note{font-size:38px;color:var(--ink-soft)}
</style>
</head>
<body>
<main class="flyer">
  <div class="illust illust--daisies" role="img" aria-label="背景に散りばめられた白いデイジーの花の模様"></div>
  <div class="abs center-glow"></div>
  <div class="illust illust--flute" role="img" aria-label="フルートを吹く女の子のイラスト"></div>
  <div class="illust illust--horn" role="img" aria-label="金色のホルンのイラスト"></div>

  <p class="abs speech">♪ベネディクト・ハウエル作曲<br>「ラ・フォンテ・ヴェルデ」<br>「星は今も瞬く」ほか<br>マルコの幻想の朝<br>夢にさそわれて…</p>

  <section class="abs ticket">
    <span class="ticket__label">【 前売り券 / 当日券 】</span>
    <span class="ticket__price">¥500</span>
    <span class="ticket__btn">チケット取り扱い</span>
    <div class="ticket__notes">
      <p>小学生未満のお客様の入場はご遠慮ください。</p>
      <p>会場内では係員の指示に従ってください。</p>
      <p>桜木楽器店・さくらホール窓口・団員まで</p>
    </div>
  </section>

  <p class="abs date">日時：2021年12月12日(日)</p>

  <h1 class="abs org">桜木市民<br>吹奏楽団</h1>
  <h2 class="abs event"><span class="event__name">ハーモニーフェスタ</span><span class="event__year">2021</span></h2>

  <p class="abs place-label">場所</p>
  <ul class="abs place">
    <li>★ 緑川県桜木市花咲町2-14</li>
    <li>★ さくら鉄道 桜木駅下車 徒歩20分</li>
    <li>★ さくらめぐりバス「文化会館」下車</li>
  </ul>

  <div class="illust illust--map" role="img" aria-label="桜木駅から桜木文化会館までの道順を示す手描きの地図"></div>
  <span class="abs map-label">MAP</span>

  <div class="abs conductor">
    <span class="conductor__role">指揮者</span>
    <span class="conductor__name">柳沼俊哉</span>
  </div>
  <div class="illust illust--conductor" role="img" aria-label="タクトを振る指揮者のイラスト"></div>

  <section class="abs contact">
    <p class="contact__title">問い合わせ</p>
    <p class="contact__row">担当 / 水野</p>
    <p class="contact__row">
      <svg width="14" height="14" viewBox="0 0 24 24" fill="none" stroke="#3f5a3a" stroke-width="2.4"><path d="M5 3h4l2 5-2.5 1.5a11 11 0 0 0 6 6L16 13l5 2v4a2 2 0 0 1-2 2A17 17 0 0 1 3 5a2 2 0 0 1 2-2z"/></svg>
      090-2716-4098
    </p>
    <p class="contact__url">https://sakuragi-brass.<br>hoshizora-web.com/</p>
  </section>

  <div class="illust illust--trumpet" role="img" aria-label="トランペットを吹く女の子のイラスト"></div>
  <div class="illust illust--piano" role="img" aria-label="ピアノの鍵盤のイラスト"></div>
  <span class="abs note" style="left:580px;top:1040px">♪</span>
  <span class="abs note" style="left:250px;top:330px;font-size:26px">♪</span>
</main>
</body>
</html>
```